Simple graphic for a book or slide presentation

We are looking for a style that suits the style of our book. It's title is Harbor. Keeping a calm course through stormy seas. There will be more line drawing/graphics in the book but how you design this image will create the style for all the other simple graphics in the book (once we decide what they are). So this one design will lead to a few more to match the style of this one. We'd like the shape of the overall graphic (i.e the arrows and words/bubbles) to be circular (not a rounded square as appears in the sample attached). Perhaps the words don't need to be in ovals or bound by anything at all; perhaps they do - let's see what you see. We'd like you to choose a font or offer many different fonts you think will capture the practical yet unconventional tone of the book. The book is teaching that managing risks in life is a life-skill that can be learned. The section of the book where this graphic will be placed is called "the power of language" - basically we are saying that thoughts, words and actions create our culture and our destiny. This insight comes from Torvel Pelloru's famous quote:
Carefully watch your thoughts, for they become your words.
Manage and watch your words, for they will become your actions.
Consider and judge your actions, for they have become your habits.
Acknowledge and watch your habits, for they shall become your values.
Understand and embrace your values, for they become your destiny.

Please change the text in the middle of the graphic to say: The Steady Course Cycle

```html
<!DOCTYPE html>
<html lang="en">
<head>
<meta charset="utf-8">
<title>The Steady Course Cycle</title>
<link rel="stylesheet" href="https://fonts.googleapis.com/css2?family=Bebas+Neue&display=swap">
<style>
  :root {
    --bg: #ecebea;
    --ink: #111111;
    --paper: #ffffff;
    --label-dark: #151515;
    --label-light: #ffffff;
    --arrow-culture: #111111;
    --arrow-thoughts: #c1202f;
    --arrow-words: #ee8a1d;
    --arrow-actions: #2a9ad6;
    --arrow-habits: #5b2d86;
    --arrow-values: #14907f;
  }
  html, body {
    margin: 0;
    padding: 0;
    width: 1200px;
    height: 1053px;
    overflow: hidden;
    background: var(--bg);
  }
  .cycle-diagram {
    display: block;
    width: 1200px;
    height: 1053px;
  }
  .stage-label {
    font-family: "Bebas Neue", "Oswald", sans-serif;
    font-size: 26px;
    text-anchor: middle;
    dominant-baseline: central;
    letter-spacing: 0.2px;
  }
  .stage-label--dark { fill: var(--label-dark); }
  .stage-label--light { fill: var(--label-light); }
  .hub-title {
    font-family: "Bebas Neue", "Oswald", sans-serif;
    font-size: 24px;
    fill: var(--paper);
    text-anchor: middle;
    dominant-baseline: central;
    letter-spacing: 1px;
  }
  .arrow line { stroke-width: 3; stroke-linecap: butt; }
  .arrow--culture line { stroke: var(--arrow-culture); }
  .arrow--culture polygon { fill: var(--arrow-culture); }
  .arrow--thoughts line { stroke: var(--arrow-thoughts); }
  .arrow--thoughts polygon { fill: var(--arrow-thoughts); }
  .arrow--words line { stroke: var(--arrow-words); }
  .arrow--words polygon { fill: var(--arrow-words); }
  .arrow--actions line { stroke: var(--arrow-actions); }
  .arrow--actions polygon { fill: var(--arrow-actions); }
  .arrow--habits line { stroke: var(--arrow-habits); }
  .arrow--habits polygon { fill: var(--arrow-habits); }
  .arrow--values line { stroke: var(--arrow-values); }
  .arrow--values polygon { fill: var(--arrow-values); }
</style>
</head>
<body>
<svg class="cycle-diagram" viewBox="0 0 1200 1053" xmlns="http://www.w3.org/2000/svg" role="img" aria-label="The Steady Course Cycle: thoughts, words, actions, habits, values, culture">
  <defs>
    <linearGradient id="fill-thoughts" x1="0" y1="0" x2="0" y2="1">
      <stop offset="0" stop-color="#e2e2e2"/><stop offset="1" stop-color="#cbcbcb"/>
    </linearGradient>
    <linearGradient id="fill-words" x1="0" y1="0" x2="0" y2="1">
      <stop offset="0" stop-color="#d8d8d8"/><stop offset="1" stop-color="#a9a9a9"/>
    </linearGradient>
    <linearGradient id="fill-actions" x1="0" y1="0" x2="0" y2="1">
      <stop offset="0" stop-color="#cdcdcd"/><stop offset="1" stop-color="#999999"/>
    </linearGradient>
    <linearGradient id="fill-habits" x1="0" y1="0" x2="0" y2="1">
      <stop offset="0" stop-color="#b9b9b9"/><stop offset="1" stop-color="#777777"/>
    </linearGradient>
    <linearGradient id="fill-values" x1="0" y1="0" x2="0" y2="1">
      <stop offset="0" stop-color="#a2a2a2"/><stop offset="1" stop-color="#626262"/>
    </linearGradient>
    <linearGradient id="fill-culture" x1="0" y1="0" x2="0" y2="1">
      <stop offset="0" stop-color="#858585"/><stop offset="1" stop-color="#363636"/>
    </linearGradient>
  </defs>

  <g class="hub">
    <circle cx="595" cy="530" r="73" fill="var(--ink)"/>
    <text class="hub-title" x="595" y="496">THE</text>
    <text class="hub-title" x="595" y="519">STEADY</text>
    <text class="hub-title" x="595" y="542">COURSE</text>
    <text class="hub-title" x="595" y="565">CYCLE</text>
  </g>

  <g class="stage stage--thoughts">
    <circle cx="595" cy="388" r="51" fill="url(#fill-thoughts)"/>
    <text class="stage-label stage-label--dark" x="595" y="388">THOUGHTS</text>
  </g>
  <g class="stage stage--words">
    <circle cx="717" cy="459" r="51" fill="url(#fill-words)"/>
    <text class="stage-label stage-label--dark" x="717" y="459">WORDS</text>
  </g>
  <g class="stage stage--actions">
    <circle cx="717" cy="601" r="51" fill="url(#fill-actions)"/>
    <text class="stage-label stage-label--dark" x="717" y="601">ACTIONS</text>
  </g>
  <g class="stage stage--habits">
    <circle cx="595" cy="672" r="51" fill="url(#fill-habits)"/>
    <text class="stage-label stage-label--dark" x="595" y="672">HABITS</text>
  </g>
  <g class="stage stage--values">
    <circle cx="473" cy="601" r="51" fill="url(#fill-values)"/>
    <text class="stage-label stage-label--light" x="473" y="601">VALUES</text>
  </g>
  <g class="stage stage--culture">
    <circle cx="473" cy="459" r="51" fill="url(#fill-culture)"/>
    <text class="stage-label stage-label--light" x="473" y="459">CULTURE</text>
  </g>

  <g class="arrow arrow--culture" transform="translate(523 414) rotate(-35)">
    <line x1="-13" y1="0" x2="5" y2="0"/><polygon points="13,0 3,-6 3,6"/>
  </g>
  <g class="arrow arrow--thoughts" transform="translate(659 411) rotate(30)">
    <line x1="-13" y1="0" x2="5" y2="0"/><polygon points="13,0 3,-6 3,6"/>
  </g>
  <g class="arrow arrow--words" transform="translate(730 528) rotate(90)">
    <line x1="-13" y1="0" x2="5" y2="0"/><polygon points="13,0 3,-6 3,6"/>
  </g>
  <g class="arrow arrow--actions" transform="translate(664 648) rotate(147)">
    <line x1="-13" y1="0" x2="5" y2="0"/><polygon points="13,0 3,-6 3,6"/>
  </g>
  <g class="arrow arrow--habits" transform="translate(528 651) rotate(205)">
    <line x1="-13" y1="0" x2="5" y2="0"/><polygon points="13,0 3,-6 3,6"/>
  </g>
  <g class="arrow arrow--values" transform="translate(458 533) rotate(-90)">
    <line x1="-13" y1="0" x2="5" y2="0"/><polygon points="13,0 3,-6 3,6"/>
  </g>
</svg>
</body>
</html>
```